Vinto PR Website

Vinto PR are a PR company with a requirement for a new website. In consultation with the client, we have defined a wireframe for a homepage to show content and functionality. A PDF of the wire frame is attached.
Current site http://www.vinto-pr.co.uk/
Updates
If you are using Stock Photography - please use PixVault
Dear All
Unfortunately, my client didn't like any of the designs submitted.
I've uploaded 3 examples of the type of photography that will appear in the carousel as supplied by the client.
Target Market(s)
Business to Business/Professionals - high value clients
Number of Pages Required
1 page
Requirements
Must have
- Colour scheme is attached as a .ase file from Kuler and can be viewed on Kuler if you search for 'VINTO PR Palette'
Corporate Typeface is Futura Book - use of Cufon is OK
Current Logo to be reatainedCall 2 Action Buttons will be controlled via the CMS so a generic background may be useful for these.
Nice to have
- RSS feeds

```html
<!DOCTYPE html>
<html lang="en">
<head>
<meta charset="utf-8">
<title>Vinto PR</title>
<link href="https://fonts.googleapis.com/css2?family=Jost:wght@300;400;500&family=Arimo:wght@400&family=Marcellus&display=swap" rel="stylesheet">
<style>
:root{
  --ink:#1a1a1a;
  --white:#ffffff;
  --teal-top:#52e3e3;
  --teal-bot:#5db5a6;
  --teal-link:#3f9a85;
  --panel:#1b1b1b;
  --text:#222222;
  --footer:#2b3229;
  --rule:#8a8a8a;
}
*{margin:0;padding:0;box-sizing:border-box}
html,body{width:960px;height:1200px;overflow:hidden;background:var(--white)}
body{position:relative;font-family:"Arimo",Arial,sans-serif;color:var(--text)}

.topbar{position:absolute;left:0;top:0;width:960px;height:72px;background:var(--ink);color:var(--white);font-family:"Jost",sans-serif;font-size:18px}
.topbar .item{position:absolute;top:24px;display:flex;align-items:center;gap:8px;white-space:nowrap}
.social-links{gap:10px}
.social-name{font-size:13px;display:flex;align-items:center;gap:4px}
.social-name i{display:inline-block;width:8px;height:8px;background:var(--teal-top)}

.brand{position:absolute;left:81px;top:104px;font-family:"Jost",sans-serif;font-weight:400;font-size:34px;line-height:40px;color:var(--ink)}

.callus{position:absolute;right:83px;top:104px;display:flex;align-items:center;gap:16px;font-family:"Jost",sans-serif;font-weight:300;font-size:27px;word-spacing:8px;color:var(--ink)}

.mainnav{position:absolute;left:81px;top:165px;width:796px;height:36px;background:linear-gradient(var(--teal-top),var(--teal-bot));box-shadow:0 1px 2px rgba(0,0,0,.3);display:flex;align-items:center;justify-content:center;gap:7px;font-family:"Jost",sans-serif;font-weight:500;font-size:14.5px;color:var(--white);white-space:nowrap}
.mainnav .sep{opacity:.9}

.services{position:absolute;left:81px;top:222px;width:796px;height:252px;display:flex}
.tabs{width:305px;list-style:none}
.tab{height:50.4px;display:flex;align-items:center;background:linear-gradient(var(--teal-top),var(--teal-bot));color:var(--white);font-family:"Jost",sans-serif;font-weight:300;font-size:21px;word-spacing:5px;border-bottom:1px solid #7fcfc6;white-space:nowrap}
.tab .label{flex:1;padding-left:28px}
.tab .arrow{width:37px;height:100%;display:flex;align-items:center;justify-content:center;border-left:1px solid rgba(0,0,0,.15);background:rgba(0,0,0,.06)}
.tab.active{background:linear-gradient(#3a3a3a,#000)}
.intro-panel{flex:1;background:var(--panel);color:var(--white);padding:16px 15px 0 15px;font-size:11.6px;line-height:16.5px}
.intro-panel h2{font-weight:400;font-size:14.5px;margin-bottom:20px}
.intro-panel p{margin-bottom:4px}

.introduction{position:absolute;left:80px;top:498px;width:530px}
.introduction h1{font-family:"Jost",sans-serif;font-weight:400;font-size:25px;margin-bottom:10px}
.introduction p{font-size:12.6px;line-height:17.2px;margin-bottom:17px}

.gallery{position:absolute;left:648px;top:501px;width:229px}
.gallery .photo{width:229px;height:102px;margin-bottom:17px;background:linear-gradient(120deg,#e9eef3,#c7d2de 55%,#2e3b52)}

.column{position:absolute;top:738px;width:262px}
.column.news{left:81px}
.column.blog{left:364px;width:257px}
.column-head{display:flex;align-items:center;gap:10px;height:42px;border-bottom:1px dotted var(--rule);font-family:"Jost",sans-serif;font-size:24px;padding-left:2px}
.entry{padding:0 6px;margin-top:10px;font-size:11px;line-height:15.2px}
.entry h3{font-weight:400;font-size:11.6px;color:var(--teal-link);margin-bottom:1px}
.blog-thumb{float:left;width:92px;height:89px;margin:0 9px 2px 0;background:linear-gradient(135deg,#2f6fb8,#7fb9e0 50%,#d7c97a)}
.more{display:block;text-align:right;font-size:12px;color:var(--teal-link);text-decoration:none;padding-right:6px}

.footer{position:absolute;left:0;top:1011px;width:960px;height:149px;background:var(--footer);font-family:"Marcellus",serif;color:#f0f0f0}
.footer ul{position:absolute;top:19px;list-style:none;font-size:13.5px;line-height:23.3px}
.footer ul.col1{left:82px}
.footer ul.col2{left:281px}
.signup{position:absolute;left:656px;top:18px}
.signup h4{display:flex;align-items:center;gap:10px;font-weight:400;font-size:18px;margin-bottom:10px}
.signup .field{width:198px;height:24px;background:var(--white);border:0;margin-bottom:12px;display:block}
.signup .btn{width:122px;height:31px;border-radius:6px;border:1px solid #555;background:linear-gradient(#4a4a4a,#050505);color:var(--white);font-family:"Marcellus",serif;font-size:16px;font-weight:700;letter-spacing:1px}
.bottom{position:absolute;left:0;top:1160px;width:960px;height:40px;background:var(--ink)}
</style>
</head>
<body>

<header class="topbar">
  <div class="item" style="left:327px">Join us on</div>
  <div class="item social-links" style="left:423px;top:27px">
    <span class="social-name"><i></i>Callo</span>
    <span class="social-name"><i></i>Chirp</span>
    <span class="social-name"><i></i>Facet</span>
  </div>
  <div class="item" style="left:597px">E-mail us
    <svg width="30" height="22" viewBox="0 0 30 22"><rect x="1" y="1" width="28" height="20" fill="#f7d54a" stroke="#c9a21d"/><path d="M1 1 L15 12 L29 1" fill="none" stroke="#c9a21d" stroke-width="1.5"/></svg>
  </div>
  <div class="item" style="left:757px">RSS Feed
    <svg width="26" height="26" viewBox="0 0 26 26"><rect x="4" y="4" width="18" height="18" rx="3" fill="#f2c230" transform="rotate(-35 13 13)"/><circle cx="10" cy="17" r="2" fill="#fff"/><path d="M9 12 A6 6 0 0 1 15 18 M9 8 A10 10 0 0 1 19 18" fill="none" stroke="#fff" stroke-width="2"/></svg>
  </div>
</header>

<div class="brand">Vinto PR</div>

<div class="callus">
  <svg width="36" height="36" viewBox="0 0 36 36"><rect width="36" height="36" rx="4" fill="#5fd8e4"/><path d="M12 8 l4 5 -2 3 c1 3 3 5 6 6 l3 -2 5 4 -2 4 c-8 0 -17 -9 -17 -17z" fill="#fff"/></svg>
  <span>Call us now 0141 555 0199</span>
</div>

<nav class="mainnav">
  <span>Home</span><span class="sep">/</span><span>Vinto Services</span><span class="sep">/</span><span>Press Office</span><span class="sep">/</span><span>Vinto Case Studies</span><span class="sep">/</span><span>Vinto People</span><span class="sep">/</span><span>Blog</span><span class="sep">/</span><span>Vinto News</span><span class="sep">/</span><span>Contact Us</span>
</nav>

<section class="services">
  <ul class="tabs">
    <li class="tab"><span class="label">Online Public Relations</span><span class="arrow"><svg width="22" height="28"><path d="M3 2 L19 14 L3 26" fill="none" stroke="#3a9f92" stroke-width="4"/></svg></span></li>
    <li class="tab active"><span class="label">Media Relations</span><span class="arrow"><svg width="22" height="28"><path d="M3 2 L19 14 L3 26" fill="none" stroke="#555" stroke-width="4"/></svg></span></li>
    <li class="tab"><span class="label">Consumer Campaigns</span><span class="arrow"><svg width="22" height="28"><path d="M3 2 L19 14 L3 26" fill="none" stroke="#3a9f92" stroke-width="4"/></svg></span></li>
    <li class="tab"><span class="label">Crisis Public Relations</span><span class="arrow"><svg width="22" height="28"><path d="M3 2 L19 14 L3 26" fill="none" stroke="#3a9f92" stroke-width="4"/></svg></span></li>
    <li class="tab"><span class="label">Internal Communications</span><span class="arrow"><svg width="22" height="28"><path d="M3 2 L19 14 L3 26" fill="none" stroke="#3a9f92" stroke-width="4"/></svg></span></li>
  </ul>
  <div class="intro-panel">
    <h2>Vinto Public Relations</h2>
    <p>Vinto Public Relations has pioneered a decidedly different approach to public relations. Newsworthy stories happen every day within your organisation but how do you unlock them?</p>
    <p>Vinto Public Relations has devised a technique called ‘thinking inside out’ which equips your team with an understanding of what makes a good story – after all, they are the ones closest to your business.<br>The results will help ensure that your organisation enjoys a strong media and on line presence by uncovering the treasure-trove of stories within your organisation.</p>
    <p>It gives every employee an understanding of public relations and empowers them to contribute fruitfully.</p>
  </div>
</section>

<section class="introduction">
  <h1>Introduction</h1>
  <p>Lorem ipsum dolor sit amet, consectetur adipiscing elit. Proin a ipsum et nisl luctus varius quis mattis dui. Mauris euismod enim eu enim scelerisque vitae lobortis quam aliquet.<br>Praesent vestibulum lorem eu elit lobortis ac cursus odio mollis. Fusce magna magna,vestibu lum eget fermentum at, blandit ut risus. Praesent blandit justo vel eros dictum sed pulvinar ligula viverra. Nam diam sem, faucibus semper placerat commodo, hendrerit at turpis.</p>
  <p>Phasellus sapien ipsum, interdum ut dapibus in, hendrerit nec nulla. Donec egestas sceleris que metus, nec placerat lectus ultrices ac. Nam sodales mollis euismod. Mauris ornare viverra dignissim. Praesent blandit justo vel eros dictum sed pulvinar ligula viverra. Nam diam sem, faucibus semper placerat commodo, hendrerit at turpis.</p>
</section>

<aside class="gallery">
  <div class="photo" role="img" aria-label="Photo of a smiling business team"></div>
  <div class="photo" role="img" aria-label="Photo of colleagues reviewing documents"></div>
  <div class="photo" role="img" aria-label="Photo of a smiling business team"></div>
  <div class="photo" role="img" aria-label="Photo of colleagues reviewing documents"></div>
</aside>

<section class="column news">
  <div class="column-head">
    <svg width="44" height="34" viewBox="0 0 44 34"><g transform="rotate(-15 22 17)"><rect x="6" y="6" width="32" height="22" fill="#eee" stroke="#999"/><path d="M10 12h24M10 16h24M10 20h24M10 24h16" stroke="#777"/></g></svg>
    Client News
  </div>
  <div class="entry">
    <h3>Lorem ipsum dolor sit amet 2010/01/10</h3>
    <p>Proin a ipsum et nisl luctus varius quis mattis dui. Mauris euismod enim eu enim scelerisque vitae lobortis quam aliquet.</p>
  </div>
  <div class="entry">
    <h3>Lorem ipsum dolor sit amet 2010/01/10</h3>
    <p>Proin a ipsum et nisl luctus varius quis mattis dui. Mauris euismod enim eu enim scelerisque vitae lobortis quam aliquet.</p>
  </div>
  <a class="more" href="#" style="margin-top:14px">more news</a>
</section>

<section class="column blog">
  <div class="column-head">
    <svg width="36" height="34" viewBox="0 0 36 34"><rect x="4" y="4" width="26" height="26" fill="#9a9a9a"/></svg>
    Blog Entry
  </div>
  <div class="entry" style="margin-top:14px">
    <div class="blog-thumb" role="img" aria-label="Blog illustration of a spiral shell with a listening banner"></div>
    <p>Lorem ipsum dolor sit amet, consectetur adipiscing elit. Proin a ipsum et nisl luctus varius quis mattis dui. Mauris euismod enim enim scelerisque vitae lobortis. Praesent vestibulum lorem eu elit lobortis ac cur sus odio mollis. Fusce magna magna...</p>
  </div>
  <a class="more" href="#" style="margin-top:14px">read more</a>
</section>

<footer class="footer">
  <ul class="col1">
    <li>Online Public Relations</li><li>Media Relations</li><li>Consumer Campaigns</li><li>Crisis Public Relations</li><li>Internal Communications</li>
  </ul>
  <ul class="col2">
    <li>Subscribe to RSS Feed</li><li>Our Facet page</li><li>Link Three</li><li>Link Four</li>
  </ul>
  <div class="signup">
    <h4>
      <svg width="34" height="34" viewBox="0 0 34 34"><rect x="4" y="4" width="22" height="27" fill="#f4f4f4" stroke="#999" transform="rotate(-8 15 17)"/><path d="M9 12h14M9 16h14M9 20h12" stroke="#888"/><path d="M16 24 L30 8" stroke="#e8b22a" stroke-width="3"/></svg>
      Enews Sign-up
    </h4>
    <input class="field" type="text" aria-label="Email address">
    <button class="btn">SUBSCIBE</button>
  </div>
</footer>
<div class="bottom"></div>

</body>
</html>
```